DELMORAN Auto Battery

We need top of the line design for a new product that we are launching, Automotive Batteries.
We are an exporter of Auto Spare parts based in China, our new products will be launched in October 2012, the website is to be presented as B2B not B2C, we deal directly with Importers all around the world.
Our vision for the website is to be Clean, elegant, smart, warm, reflects confidence and trust..therefore, the choice of themes, colors, fonts and graphics should take into considerations all above.
Since there are hundreds of Battery types, specs, sizes, weight...etc, we will need a upload template that will enable us to upload, modify and manipulate the data of the batteries.
Car battery importers
Automotive

```html
<!DOCTYPE html>
<html lang="en">
<head>
<meta charset="utf-8">
<title>DELMORAN Auto Battery</title>
<link href="https://fonts.googleapis.com/css2?family=Exo+2:wght@600&family=Signika:wght@300;400&family=Arimo:ital,wght@0,400;1,400;1,700&display=swap" rel="stylesheet">
<style>
:root{
  --top-strip:#1d3a4a;
  --hero-top:#2d5468;
  --hero-bottom:#5d8da5;
  --logo:#0d2b3b;
  --nav-text:#ffffff;
  --gold:#e8c54c;
  --hero-ink:#0c1c26;
  --band-top:#f1f1f1;
  --band-bottom:#d9d9d9;
  --title-blue:#1b4a63;
  --price:#2a4a82;
  --body-grey:#6a6a6a;
  --heading-grey:#444;
  --btn-face:#dfe5e9;
  --footer:#0c2233;
  --footer-link:#8fa3b0;
}
*{margin:0;padding:0;box-sizing:border-box}
html,body{width:1019px;height:1200px;overflow:hidden}
body{position:relative;background:#fff;font-family:Arimo,Arial,sans-serif}
.abs{position:absolute}

.hero{left:0;top:0;width:1019px;height:444px;background:linear-gradient(180deg,var(--hero-top) 0%,#4a7a92 55%,var(--hero-bottom) 100%)}
.top-strip{left:0;top:0;width:1019px;height:10px;background:var(--top-strip)}
.logo{left:168px;top:28px;font-family:"Exo 2",sans-serif;font-weight:600;font-size:27px;color:var(--logo);letter-spacing:1px}
.logo-rule{left:338px;top:54px;width:510px;height:1px;background:#6f93a5}
.quick{top:24px;display:flex;align-items:center;gap:5px;font-size:8px;line-height:11px;color:#fff}
.quick i{display:block;width:24px;height:24px;border-radius:50%;background:radial-gradient(circle at 40% 35%,#fff,#c9d5db 70%,#8ea3ae)}
.nav{left:182px;top:76px;width:643px;height:28px;border-bottom:1px solid #6f93a5}
.nav a{position:absolute;top:2px;font-family:Signika,sans-serif;font-weight:300;font-size:13px;color:var(--nav-text);text-decoration:none}
.nav-marker{left:210px;top:98px;width:0;height:0;border-left:4px solid transparent;border-right:4px solid transparent;border-bottom:5px solid #1d3a4a}
.call{left:678px;top:121px;font-size:13px;color:var(--gold)}
.hero-kicker{left:210px;top:171px;font-family:Signika,sans-serif;font-weight:300;font-size:20px;color:#e8eef1}
.hero-title{left:212px;top:204px;font-family:Signika,sans-serif;font-weight:300;font-size:22px;color:#f1f4f6;font-variant:small-caps;letter-spacing:3px}
.hero-copy{left:193px;top:248px;width:266px;font-size:11.3px;line-height:19px;color:var(--hero-ink);text-align:justify}
.btn-hero{left:370px;top:351px;width:86px;height:23px;border:1px solid #8fb0c0;background:#4d7f98;color:#d8e6ec;font-size:11px;text-align:center;line-height:21px}
.hero-photo{left:500px;top:160px;width:324px;height:284px;border-radius:6px 6px 0 0;background:linear-gradient(180deg,#6d8d9e 0%,#9fb2bc 45%,#c9d3d8 100%)}

.products{left:0;top:444px;width:1019px;height:286px;background:linear-gradient(180deg,var(--band-top),var(--band-bottom))}
.products-title{left:0;top:450px;width:992px;text-align:center;font-family:Signika,sans-serif;font-weight:300;font-size:20px;color:var(--title-blue)}
.pager{left:772px;top:464px;font-size:10px;color:#333}
.products-rule{left:166px;top:480px;width:678px;height:1px;background:#b9b9b9}
.card{width:105px;height:100px;background:linear-gradient(180deg,#e8e8e8,#d8d8d8);border:1px solid #cfcfcf}
.card .shot{position:absolute;left:6px;top:6px;width:93px;height:68px;background:linear-gradient(180deg,#5b6166,#b9bec2);border:1px solid #c5c5c5}
.card .shot.light{background:linear-gradient(180deg,#aab0b4,#eceeee)}
.card .price{position:absolute;left:7px;top:78px;font-family:Signika,sans-serif;font-weight:300;font-size:10px;color:var(--price)}

.section-head{font-family:Signika,sans-serif;font-weight:300;color:var(--heading-grey)}
.welcome-head{left:166px;top:748px;font-size:16px}
.reviews-head{left:589px;top:750px;font-size:13.5px}
.welcome-copy{left:168px;top:780px;width:382px;font-size:8.1px;line-height:11.6px;color:var(--body-grey);text-align:justify}
.welcome-lead{left:168px;top:902px;width:382px;font-size:8.1px;line-height:11.6px;color:#555;font-style:italic;font-weight:700;text-align:justify}
.btn{height:24px;width:87px;background:linear-gradient(180deg,#eef1f3,var(--btn-face));border-bottom:2px solid #aab5bb;font-size:11px;color:#1d3a4a;text-align:center;line-height:23px}
.review{left:590px;width:249px;font-size:8.1px;line-height:11.6px;color:var(--body-grey);text-align:justify}
.review em{float:right;font-size:7.5px;color:#2a4a82;font-weight:700}
.review-rule{left:590px;width:249px;height:1px;background:#dcdcdc}

.footer{left:0;top:990px;width:1019px;height:210px;background:var(--footer)}
.subscribe{left:175px;top:1019px;width:263px;height:47px;background:#fff;box-shadow:0 2px 6px rgba(0,0,0,.5)}
.subscribe-tail{left:208px;top:1066px;width:0;height:0;border-left:7px solid transparent;border-right:7px solid transparent;border-top:10px solid #fff}
.email-field{left:182px;top:1032px;width:206px;height:20px;border:1px solid #bbb;background:#ececec;font-size:8px;color:#444;padding:5px 12px}
.email-send{left:395px;top:1032px;width:36px;height:20px;background:#1d2a33}
.subscribe-note{left:183px;top:1085px;font-size:9.5px;font-style:italic;color:#aab4ba}
.foot-links{list-style:none;font-size:7.8px;line-height:18.3px;color:var(--footer-link)}
.foot-links li::before{content:"\25B8";font-size:6px;color:#4b6677;margin-right:6px}
.social{left:795px;width:28px;height:28px;border-radius:50%;background:#7e8a92}
.bottom-bar{left:184px;top:1125px;width:651px;height:28px;border:1px solid #2c4b5e;font-size:7.4px;color:#b6c2c9;line-height:26px;padding:0 8px}
.bottom-bar span{float:right}
</style>
</head>
<body>

<div class="abs hero"></div>
<div class="abs top-strip"></div>
<div class="abs logo">DELMORAN</div>
<div class="abs logo-rule"></div>

<div class="abs quick" style="left:566px"><i></i><span>24/7 Customer<br>Services</span></div>
<div class="abs quick" style="left:660px"><i></i><span>Order<br>Now</span></div>
<div class="abs quick" style="left:723px"><i></i><span>Customer<br>Support</span></div>
<div class="abs quick" style="left:800px"><i></i><span>Live<br>Chat</span></div>

<nav class="abs nav">
  <a style="left:20px">Home</a>
  <a style="left:76px">About Us</a>
  <a style="left:149px">Our Products</a>
  <a style="left:243px">Order Now</a>
  <a style="left:324px">Reviews</a>
  <a style="left:395px">Testimonials</a>
  <a style="left:486px">Newly Launched</a>
  <a style="left:597px">Contact</a>
</nav>
<div class="abs nav-marker"></div>

<div class="abs call">Call Us On: 123-456-7890</div>
<div class="abs hero-kicker">For Fast &amp; Best Performance</div>
<div class="abs hero-title">Auto Batteries</div>
<p class="abs hero-copy">Lorem ipsum dolor sit amet, consectetur adipisicing elit, sed do eiusmod tempor incididunt ut labore et dolore magna aliqua. Ut enim ad minim veniam, quis nostrud exercitation ullamco laboris nisi ut aliquip ex ea commodo consequat.</p>
<div class="abs btn-hero">Read More</div>
<div class="abs hero-photo" role="img" aria-label="Photo of a car battery with red and blue terminals"></div>

<div class="abs products"></div>
<div class="abs products-title">Our Products</div>
<div class="abs pager">Previous &nbsp;|&nbsp; Next</div>
<div class="abs products-rule"></div>

<div class="abs card" style="left:166px;top:495px"><div class="shot" role="img" aria-label="Product photo of a black car battery"></div><span class="price">Price $256</span></div>
<div class="abs card" style="left:283px;top:495px"><div class="shot" role="img" aria-label="Product photo of a black car battery"></div><span class="price">Price $256</span></div>
<div class="abs card" style="left:398px;top:495px"><div class="shot light" role="img" aria-label="Product photo of a white car battery"></div><span class="price">Price $256</span></div>
<div class="abs card" style="left:512px;top:495px"><div class="shot" role="img" aria-label="Product photo of a dark car battery"></div><span class="price">Price $256</span></div>
<div class="abs card" style="left:626px;top:495px"><div class="shot" role="img" aria-label="Product photo of a dark car battery"></div><span class="price">Price $256</span></div>
<div class="abs card" style="left:742px;top:495px"><div class="shot light" role="img" aria-label="Product photo of a white car battery"></div><span class="price">Price $256</span></div>

<div class="abs card" style="left:166px;top:616px"><div class="shot" role="img" aria-label="Product photo of a black car battery"></div><span class="price">Price $256</span></div>
<div class="abs card" style="left:283px;top:616px"><div class="shot" role="img" aria-label="Product photo of a black car battery"></div><span class="price">Price $256</span></div>
<div class="abs card" style="left:398px;top:616px"><div class="shot light" role="img" aria-label="Product photo of a white car battery"></div><span class="price">Price $256</span></div>
<div class="abs card" style="left:512px;top:616px"><div class="shot" role="img" aria-label="Product photo of a dark car battery"></div><span class="price">Price $256</span></div>
<div class="abs card" style="left:626px;top:616px"><div class="shot" role="img" aria-label="Product photo of a dark car battery"></div><span class="price">Price $256</span></div>
<div class="abs card" style="left:742px;top:616px"><div class="shot light" role="img" aria-label="Product photo of a white car battery"></div><span class="price">Price $256</span></div>

<h2 class="abs section-head welcome-head">Welcome To Our Site....</h2>
<p class="abs welcome-copy">Lorem ipsum dolor sit amet, consectetur adipisicing elit, sed do eiusmod tempor incididunt ut labore et dolore magna aliqua. Ut enim ad minim veniam, quis nostrud exercitation ullamco laboris nisi ut aliquip ex ea commodo consequat. Duis aute irure dolor in reprehenderit in voluptate velit esse cillum dolore eu fugiat nulla pariatur. Excepteur sint occaecat cupidatat non proident, sunt in culpa qui officia deserunt mollit anim id est laborum. Lorem ipsum dolor sit amet, consectetur adipisicing elit, sed do eiusmod tempor incididunt ut labore et dolore magna aliqua. Ut enim ad minim veniam, quis nostrud exercitation ullamco laboris nisi ut aliquip ex ea commodo consequat. Duis aute irure dolor in reprehenderit in voluptate velit esse cillum dolore eu fugiat nulla pariatur. Excepteur sint occaecat cupidatat non proident, sunt in culpa qui officia deserunt mollit anim id est laborum.</p>
<p class="abs welcome-lead">Lorem ipsum dolor sit amet, consectetur adipisicing elit, sed do eiusmod tempor incididunt ut labore et dolore magna aliqua. Ut enim ad minim veniam, quis nostrud exercitation ullamco laboris nisi ut aliquip ex ea commodo consequat.</p>
<div class="abs btn" style="left:461px;top:944px">Read More</div>

<h2 class="abs section-head reviews-head">Customer Reviews</h2>
<p class="abs review" style="top:781px">Lorem ipsum dolor sit amet, consectetur adipisicing elit, sed do eiusmod tempor incididunt ut labore et dolore magna aliqua. Ut enim ad minim veniam, quis nostrud exercitation ullamco laboris nisi ut aliquip ex ea commodo consequat. <em>More+</em></p>
<div class="abs review-rule" style="top:838px"></div>
<p class="abs review" style="top:847px">Lorem ipsum dolor sit amet, consectetur adipisicing elit, sed do eiusmod tempor incididunt ut labore et dolore magna aliqua. <em>More+</em></p>
<div class="abs review-rule" style="top:881px"></div>
<p class="abs review" style="top:890px">Lorem ipsum dolor sit amet, consectetur adipisicing elit, sed do eiusmod tempor incididunt ut labore et dolore magna aliqua. Ut enim ad minim veniam, quis nostrud exercitation ullamco laboris nisi ut aliquip ex ea commodo consequat. <em>More+</em></p>
<div class="abs btn" style="left:754px;top:944px">View More</div>

<footer class="abs footer"></footer>
<div class="abs subscribe"></div>
<div class="abs subscribe-tail"></div>
<div class="abs email-field">Enter Your Email Id</div>
<div class="abs email-send">
  <svg width="36" height="20" viewBox="0 0 36 20"><rect x="12" y="6" width="12" height="8" fill="#e6e6e6"/><path d="M12 6 L18 11 L24 6" stroke="#555" fill="none" stroke-width="1"/></svg>
</div>
<div class="abs subscribe-note">Enter Your Details For Subscribe With Us</div>

<ul class="abs foot-links" style="left:508px;top:1013px">
  <li>Company Profile</li><li>Our Products</li><li>Testimonials</li><li>Shop Now</li>
</ul>
<ul class="abs foot-links" style="left:644px;top:1013px">
  <li>Contact us</li><li>24*7 Customer Services</li><li>Live Chat</li><li>Customer Support</li>
</ul>

<div class="abs social" style="top:1008px"></div>
<div class="abs social" style="top:1041px"></div>
<div class="abs social" style="top:1074px"></div>

<div class="abs bottom-bar">Home | About Us | Our Products | Order Now | Reviews | Testimonials | Newly Launched | Contact <span>Copyright Statement</span></div>

</body>
</html>
```